Poster of Insipirational Quotes

Attached is a list of leadership quotes from Arlen Drubeck. I would like a poster made, incorporating whatever design elements you like, potentially including Arlen's face, and one or more of the quotes. I intend to print this out in A3 or larger to hang on my wall.

The quotes are:

Being responsible sometimes means pissing people off.

The day soldiers stop bringing you their problems is the day you have stopped leading them.

Don't be buffaloed by experts and elites. Experts often possess more data than judgment. Elites can become so inbred that they produce hemophiliacs who bleed to death as soon as they are nicked by the real world.

Don't be afraid to challenge the pros, even in their own backyard.

Never neglect details. When everyone's mind is dulled or distracted the leader must be doubly vigilant.

You don't know what you can get away with until you try.

Keep looking below surface appearances. Don't shrink from doing so (just) because you might not like what you find.

Organization doesn't really accomplish anything. Plans don't accomplish anything, either. Theories of management don't much matter. Endeavors succeed or fail because of the people involved. Only by attracting the best people will you accomplish great deeds.

Organization charts and fancy titles count for next to nothing.

Never let your ego get so close to your position that when your position goes, your ego goes with it.

Fit no stereotypes. Don't chase the latest management fads. The situation dictates which approach best accomplishes the team's mission.

Perpetual optimism is a force multiplier.

Look for intelligence and judgment, and most critically, a capacity to anticipate, to see around corners. Also look for loyalty, integrity, a high energy drive, a balanced ego, and the drive to get things done.

Great leaders are almost always great simplifiers, who can cut through argument, debate and doubt, to offer a solution everybody can understand.

The commander in the field is always right and the rear echelon is wrong, unless proved otherwise.

Have fun in your command. Don't always run at a breakneck pace. Take leave when you've earned it: Spend time with your families. Corollary: surround yourself with people who take their work seriously, but not themselves, those who work hard and play hard.

Command is lonely.

Leadership is the art of accomplishing more than the science of management
says is possible.
Updates

I need to modify the specification based on the designs that I've seen.

Target Market(s)

Executive Office

Colors

Designer to choose colors to be used in the design.

Requirements
Must have
• Quotes

```html
<!DOCTYPE html>
<html lang="en">
<head>
<meta charset="utf-8">
<title>Leadership Quotes — Arlen Drubeck</title>
<link rel="stylesheet" href="https://fonts.googleapis.com/css2?family=Oswald:wght@400;700&display=swap">
<style>
  :root {
    --frame: #c3c3c3;
    --paper: #ffffff;
    --ink: #141414;
    --mark: #bdbdbd;
    --portrait-light: #e2e2e2;
    --portrait-dark: #c8c8c8;
  }
  html, body {
    margin: 0;
    padding: 0;
    width: 848px;
    height: 1200px;
    overflow: hidden;
    background: var(--frame);
  }
  .poster {
    position: relative;
    width: 848px;
    height: 1200px;
    background: var(--frame);
  }
  .sheet {
    position: absolute;
    left: 22px;
    top: 22px;
    width: 798px;
    height: 1148px;
    background: var(--paper);
    overflow: hidden;
  }
  .portrait-area {
    position: absolute;
    left: 55px;
    top: 118px;
    width: 705px;
    height: 830px;
    border-radius: 46% 40% 8% 12% / 40% 36% 4% 6%;
    background: radial-gradient(ellipse at 55% 40%, var(--portrait-dark) 0%, var(--portrait-light) 75%, var(--paper) 100%);
    opacity: 0.75;
  }
  .quote-mark {
    position: absolute;
    font-family: "Oswald", sans-serif;
    font-weight: 700;
    font-size: 190px;
    line-height: 1;
    color: var(--mark);
  }
  .quote-mark--open { left: 68px; top: 10px; }
  .quote-mark--close { left: 650px; top: 1010px; }
  .quotes {
    position: absolute;
    left: 72px;
    top: 73px;
    margin: 0;
    padding: 0;
    list-style: none;
    font-family: "Oswald", sans-serif;
    font-weight: 400;
    font-size: 15px;
    line-height: 23px;
    letter-spacing: -0.1px;
    color: var(--ink);
    white-space: nowrap;
  }
  .quotes li { margin: 0 0 23px; }
  .quotes li:last-child { margin-bottom: 0; }
</style>
</head>
<body>
<main class="poster">
  <div class="sheet">
    <div class="portrait-area" role="img" aria-label="Grey silhouette portrait of Arlen Drubeck in profile"></div>
    <span class="quote-mark quote-mark--open" aria-hidden="true">“</span>
    <ul class="quotes">
      <li>Being responsible sometimes means pissing people off.</li>
      <li>The day soldiers stop bringing you their problems is the day you have stopped leading them.</li>
      <li>Don't be buffaloed by experts and elites. Experts often possess more data than judgment. Elites can become<br>so inbred that they produce hemophiliacs who bleed to death as soon as they are nicked by the real world.</li>
      <li>Don't be afraid to challenge the pros, even in their own backyard.</li>
      <li>Never neglect details. When everyone's mind is dulled or distracted the leader must be doubly vigilant.</li>
      <li>You don't know what you can get away with until you try.</li>
      <li>Keep looking below surface appearances. Don't shrink from doing so (just) because<br>you might not like what you find.</li>
      <li>Organization doesn't really accomplish anything. Plans don't accomplish anything, either.<br>Theories of management don't much matter. Endeavors succeed or fail because of the<br>people involved. Only by attracting the best people will you accomplish great deeds.</li>
      <li>Organization charts and fancy titles count for next to nothing.</li>
      <li>Never let your ego get so close to your position that when your position goes, your ego goes with it.</li>
      <li>Fit no stereotypes. Don't chase the latest management fads. The situation dictates which<br>approach best accomplishes the team's mission.</li>
      <li>Perpetual optimism is a force multiplier.</li>
      <li>Look for intelligence and judgment, and most critically, a capacity to anticipate, to see around corners.<br>Also look for loyalty, integrity, a high energy drive, a balanced ego, and the drive to get things done.</li>
      <li>Great leaders are almost always great simplifiers, who can cut through argument, debate and doubt,<br>to offer a solution everybody can understand.</li>
      <li>The commander in the field is always right and the rear echelon is wrong, unless proved otherwise.</li>
      <li>Have fun in your command. Don't always run at a breakneck pace. Take leave when you've earned it:<br>Spend time with your families. Corollary: surround yourself with people who take their work<br>seriously, but not themselves, those who work hard and play hard.</li>
      <li>Command is lonely.</li>
      <li>Leadership is the art of accomplishing more than the science of management says is possible.</li>
    </ul>
    <span class="quote-mark quote-mark--close" aria-hidden="true">”</span>
  </div>
</main>
</body>
</html>
```